Create a book cover - front, back and spine - for a book aimed at high school and college graduates. The book poses a series of questions and possible ways of answering these questions.

Size 5" x 8" with a .45" spine.

Target Market(s)

18-25 year old high school and college graduates.

Industry/Entity Type

High School

Requirements
Must have
• Front cover - image(s) related to graduation, text "Seven Crossroads Before Your Next Chapter" and the author "Tomas Quillan"

Back cover - see attachment. Text will be altered later but right now I just need filler spots.

```html
<!DOCTYPE html>
<html lang="en">
<head>
<meta charset="utf-8">
<title>Seven Crossroads Before Your Next Chapter – Book Cover</title>
<link rel="stylesheet" href="https://fonts.googleapis.com/css2?family=Rokkitt:wght@400;500&family=Glegoo&family=Open+Sans:wght@400&display=swap">
<style>
  :root {
    --page-bg: #ffffff;
    --frame: #2e2a6e;
    --accent-green: #5c8a2a;
    --navy: #28286a;
    --ink: #111111;
    --red: #d0202b;
    --quote-red: #c8141e;
    --fold-shadow: #c9c9c9;
    --fold-light: #f7f7f7;
    --art-light: #f2f2f2;
    --art-mid: #bfbfbf;
    --art-dark: #5a5a5a;
  }
  html, body {
    margin: 0;
    padding: 0;
    width: 1200px;
    height: 961px;
    overflow: hidden;
    background: var(--page-bg);
  }
  .canvas {
    position: relative;
    width: 1200px;
    height: 961px;
    font-family: "Rokkitt", Georgia, serif;
    color: var(--ink);
  }
  .band-top, .band-bottom {
    position: absolute;
    left: 0;
    width: 1200px;
    background: var(--accent-green);
  }
  .band-top { top: 0; height: 6px; }
  .band-bottom { bottom: 0; height: 8px; }

  .corner-fold {
    position: absolute;
    left: 0;
    top: 6px;
    width: 160px;
    height: 140px;
  }
  .sheet-caption {
    position: absolute;
    left: 0;
    top: 26px;
    width: 1200px;
    margin: 0;
    text-align: center;
    font-family: "Open Sans", Verdana, sans-serif;
    font-size: 16px;
    font-weight: 400;
    color: var(--ink);
  }

  .cover-spread {
    position: absolute;
    left: 50px;
    top: 92px;
    width: 1095px;
    height: 836px;
    border: 1px solid var(--frame);
    box-sizing: border-box;
  }

  /* Back cover */
  .back-cover {
    position: absolute;
    left: 29px;
    top: 26px;
    width: 469px;
    font-size: 15px;
    line-height: 21px;
  }
  .back-heading {
    margin: 0 0 18px;
    font-size: 15.5px;
    font-weight: 400;
    color: var(--navy);
  }
  .back-blurb {
    margin: 0 0 18px;
    text-indent: 24px;
    text-align: justify;
  }
  .endorsement { margin: 0 0 19px; }
  .endorsement-quote {
    margin: 0;
    text-align: justify;
  }
  .endorsement-source {
    display: block;
    color: var(--quote-red);
  }
  .barcode-area {
    position: absolute;
    left: 244px;
    top: 697px;
    width: 248px;
    height: 102px;
    border: 1px solid var(--ink);
    box-sizing: border-box;
    display: flex;
    align-items: center;
    justify-content: center;
    font-size: 15px;
  }

  /* Spine */
  .spine-title, .spine-author {
    position: absolute;
    transform-origin: left top;
    transform: rotate(90deg);
    white-space: nowrap;
  }
  .spine-title {
    left: 561px;
    top: 30px;
    font-size: 18px;
    color: var(--navy);
  }
  .spine-author {
    left: 540px;
    top: 700px;
    font-size: 18px;
    color: var(--quote-red);
    text-decoration: underline;
    text-underline-offset: 4px;
    text-decoration-thickness: 1px;
  }

  /* Front cover */
  .front-title {
    position: absolute;
    left: 575px;
    top: 24px;
    width: 420px;
    margin: 0;
    text-align: center;
    font-weight: 400;
  }
  .front-title span { display: block; white-space: nowrap; }
  .title-line-one {
    font-size: 48px;
    line-height: 60px;
    color: var(--navy);
    font-weight: 500;
  }
  .title-line-two {
    font-size: 48px;
    line-height: 64px;
    color: var(--ink);
    font-weight: 500;
  }
  .title-line-three {
    font-family: "Glegoo", Georgia, serif;
    font-size: 92px;
    line-height: 120px;
    color: var(--red);
  }
  .cap-art {
    position: absolute;
    left: 1000px;
    top: 62px;
    width: 82px;
    height: 50px;
  }
  .book-art {
    position: absolute;
    left: 596px;
    top: 309px;
    width: 479px;
    height: 422px;
  }
  .front-author {
    position: absolute;
    left: 943px;
    top: 762px;
    font-size: 23px;
    color: var(--quote-red);
    border-bottom: 1px solid var(--quote-red);
    padding-bottom: 1px;
    white-space: nowrap;
  }
</style>
</head>
<body>
<div class="canvas">
  <div class="band-top"></div>

  <svg class="corner-fold" viewBox="0 0 160 140" aria-hidden="true">
    <defs>
      <linearGradient id="foldTone" x1="0" y1="0" x2="1" y2="1">
        <stop offset="0" stop-color="var(--fold-light)"/>
        <stop offset="1" stop-color="var(--fold-shadow)"/>
      </linearGradient>
    </defs>
    <polygon points="8,0 150,0 8,128" fill="var(--page-bg)" stroke="var(--fold-shadow)" stroke-width="1"/>
    <polygon points="150,0 8,128 12,132 154,4" fill="url(#foldTone)"/>
  </svg>
  <p class="sheet-caption">Tomas Book Cover design Sample</p>

  <section class="cover-spread">
    <div class="back-cover">
      <h2 class="back-heading">Seven Crossroads Before Your Next Chapter</h2>
      <p class="back-blurb">This graduation gift is blah dog and cat and now is the time for all good men to come to the aid of their countries and sometimes when it rains it pours and then there are other words that are interesting and they come next and then we put in a period. This period shows that there are different sentences, and probably I’ll put a bit more thought into this summary paragraph at some point, but right now it’s just not a priority so I’m sticking with this for now, but within the week it should be all done and we can make the adjustments at that point.</p>

      <div class="endorsement">
        <p class="endorsement-quote">“This was one of the best books I ever read because it had consonants and vowels and a variety of punctuation marks!”</p>
        <span class="endorsement-source">Harlan Pettigrew, Brightwater State University – Class of 2013</span>
      </div>
      <div class="endorsement">
        <p class="endorsement-quote">“If only I’d have answered these questions after I’d graduated, I might not be living in my parents basement trying to invent a new synonym for ‘fetch’”</p>
        <span class="endorsement-source">Delia Marchetti, Quite Notable College – Class of 2046</span>
      </div>
      <div class="endorsement">
        <p class="endorsement-quote">“This book has just the right balance of history and economics and totally made up stuff that it makes his theories both palpable and alluring to Type 1 Diabetics and furniture salesmen.”</p>
        <span class="endorsement-source">Ferris Oakhurst, Linden Vale University – Class of 2008</span>
      </div>
      <div class="endorsement">
        <p class="endorsement-quote">“A great book! I’ll read it in a few weeks if I have nothing else to do! I like exclamation marks!”</p>
        <span class="endorsement-source">Winnie Wickersham, Harbor Ridge High School, Class of 2012</span>
      </div>
    </div>

    <div class="barcode-area">Bar Code</div>

    <div class="spine-title">Seven Crossroads Before Your Next Chapter</div>
    <div class="spine-author">Tomas Quillan</div>

    <h1 class="front-title">
      <span class="title-line-one">Seven Crossroads</span>
      <span class="title-line-two">Before Your Next</span>
      <span class="title-line-three">Chapter</span>
    </h1>

    <svg class="cap-art" role="img" aria-label="Graduation mortarboard cap with a rolled diploma" viewBox="0 0 82 50">
      <defs>
        <linearGradient id="capTone" x1="0" y1="0" x2="0" y2="1">
          <stop offset="0" stop-color="#3a3a3a"/>
          <stop offset="1" stop-color="#e6e6e6"/>
        </linearGradient>
      </defs>
      <rect width="82" height="50" rx="8" fill="url(#capTone)"/>
    </svg>

    <svg class="book-art" role="img" aria-label="Open book with fanned pages and a glossy liquid question mark rising above it" viewBox="0 0 479 422">
      <defs>
        <radialGradient id="bookTone" cx="0.5" cy="0.6" r="0.6">
          <stop offset="0" stop-color="var(--art-light)"/>
          <stop offset="0.7" stop-color="var(--art-mid)"/>
          <stop offset="1" stop-color="var(--art-dark)"/>
        </radialGradient>
      </defs>
      <rect width="479" height="422" rx="20" fill="url(#bookTone)"/>
    </svg>

    <div class="front-author">Tomas Quillan</div>
  </section>

  <div class="band-bottom"></div>
</div>
</body>
</html>
```